Mobile Home Page Design for “Zarvo for Plumbers” – in Figma

PipeDashly: Fast, Reliable Emergency Plumbing at Your Fingertips

PipeDashly is a streamlined platform connecting homeowners with trusted, local plumbers for urgent repairs—whether it’s a burst pipe, leak, or blocked toilet. Designed for speed and peace of mind, our homepage will be clean, modern, and mobile-optimized to guide users from problem to solution in minutes.

Our primary users are homeowners in stressful situations who care most about price transparency and how fast help can arrive. Bookings are made exclusively online, so the user experience must instill confidence and eliminate hesitation.

The call-to-action should be immediate and persuasive—"See Prices & Book" will be prominently featured as the main CTA. Additional trust-builders could include:

A simple 3-step booking illustration (Tell us what’s wrong → See prices → Get a plumber)
Customer reviews or “Trusted by 10,000+ homeowners” badges

Display real-time availability ("Next plumber available in 40 minutes")
Price estimates upfront—with clear service types

Target Market(s)

Home Owners: 35-65 Years old.

Industry/Entity Type

Home Services.

Number of Pages Required

1 page

Font styles to use
Sans Serif

Colors
0054AA
0677BA
7BADD7
CADEEF
E8F1F8
FFF300
FFF600
FEFA6F
FFFEC7
FFFEE8

Requirements
Nice to have
• Map showing that plumbers are nearby. Trustworthy look and feel. Blue/Red or Blue/Yellow.

```html
<!DOCTYPE html>
<html lang="en">
<head>
<meta charset="utf-8">
<title>PipeDashly – Home Page Layouts</title>
<link href="https://fonts.googleapis.com/css2?family=Open+Sans:wght@400;600;700&display=swap" rel="stylesheet">
<style>
:root{
  --blue:#1287f0;
  --blue-dark:#0a6fd1;
  --navy:#0c2340;
  --ink:#16202e;
  --muted:#7a8594;
  --tint:#eef3fa;
  --line:#dfe6ef;
  --white:#ffffff;
  --board:#2a2a2a;
}
*{box-sizing:border-box;margin:0;padding:0}
html,body{width:718px;height:1200px;overflow:hidden;background:var(--board)}
body{font-family:"Open Sans",Arial,sans-serif;color:var(--ink)}
.stage{position:relative;width:1484px;height:2480px;transform:scale(0.48383);transform-origin:0 0}
.artboard{position:absolute;background:var(--white);overflow:hidden}
.a{position:absolute}
.center{text-align:center}
.h{font-weight:600;color:var(--ink);line-height:1.25}
.blue{color:var(--blue)}
.white{color:var(--white)}
.p{color:var(--muted);line-height:1.45}
.btn{position:absolute;display:flex;align-items:center;justify-content:center;border-radius:3px;font-weight:600;white-space:nowrap}
.btn-fill{background:var(--blue);color:var(--white)}
.btn-out{border:1px solid var(--blue);color:var(--blue);background:var(--white)}
.btn-navy{background:var(--navy);color:var(--white);border-radius:8px}
.pill{position:absolute;border:1px solid var(--ink);border-radius:6px;font-size:3.5px;font-weight:700;padding:1px 5px;letter-spacing:.2px}
.photo{position:absolute;background:linear-gradient(135deg,#c9ccd2,#8f98a6 55%,#4d5f78)}
.photo-warm{background:linear-gradient(135deg,#e9e6e1,#b7a795 55%,#5b6e8c)}
.map{position:absolute;background:linear-gradient(140deg,#e7ebe6,#d6e3d2 45%,#e9ece9)}
.map-river{background:linear-gradient(150deg,#e8e4dc,#d9e2d3 40%,#8fb2ee 60%,#e6e4de)}
.card{position:absolute;background:var(--white);box-shadow:0 1px 4px rgba(20,40,70,.12);border-radius:3px}
.stripe{position:absolute;height:5px;background:var(--blue)}
.icon-ring{position:absolute;border-radius:50%;border:1px solid var(--line);background:var(--white);display:flex;align-items:center;justify-content:center}
.num{position:absolute;background:var(--white);border:1px solid var(--line);border-radius:50%;font-size:4px;font-weight:700;display:flex;align-items:center;justify-content:center}
.check{position:absolute;width:6px;height:6px;border-radius:1px;background:var(--blue)}
.logo{position:absolute;display:flex;align-items:center;gap:2px;font-weight:700;color:var(--ink)}
.logo i{display:block;background:var(--blue);border-radius:1px}
.badge-shape{position:absolute;border-radius:3px;background:#cfd6df}
.social{position:absolute;width:6px;height:6px;border-radius:50%;background:var(--white)}
.chev{position:absolute;width:10px;height:10px;border-radius:50%;border:1px solid var(--line)}
.rule{position:absolute;height:1px;background:var(--line)}
.footer{position:absolute;background:var(--navy);color:#cfd8e6}
.quote{position:absolute;color:var(--blue);font-weight:700;font-family:Georgia,serif}
.avatar{position:absolute;border-radius:50%;background:linear-gradient(135deg,#c7b59f,#5d6a7c)}
</style>
</head>
<body>
<div class="stage">

<!-- ============ MOBILE: upper section ============ -->
<section class="artboard mobile-top" style="left:181px;top:164px;width:204px;height:1913px">
  <div class="a" style="left:0;top:0;width:204px;height:33px;border-bottom:1px solid var(--line)"></div>
  <div class="logo" style="left:12px;top:13px;font-size:8px"><i style="width:5px;height:9px"></i>PipeDashly</div>
  <svg class="a" style="left:178px;top:14px" width="12" height="9"><path d="M1 1h10M1 4.5h10M1 8h10" stroke="#16202e" stroke-width="1.2"/></svg>

  <div class="a h center" style="left:0;top:52px;width:204px;font-size:14px">Plumbing Emergency?</div>
  <div class="a h center blue" style="left:0;top:72px;width:204px;font-size:14px">Get Help in Minutes.</div>
  <div class="a p center" style="left:16px;top:102px;width:172px;font-size:5px">Book a trusted, local plumber near you—available 24/7 with instant response and up-front pricing. No delays. No surprises.</div>
  <div class="btn btn-out" style="left:28px;top:134px;width:64px;height:18px;font-size:5px">Get Instant Help</div>
  <div class="btn btn-fill" style="left:100px;top:134px;width:76px;height:18px;font-size:5px">Book a Plumber Now</div>

  <div class="a h center" style="left:0;top:180px;width:204px;font-size:13px">Why Choose<br>PipeDashly?</div>
  <div class="a" style="left:0;top:223px;width:204px;height:51px;background:var(--blue)"></div>
  <svg class="a" style="left:24px;top:229px" width="16" height="16"><circle cx="8" cy="8" r="7" fill="none" stroke="#fff"/><circle cx="8" cy="6" r="2.2" fill="#fff"/><path d="M4 12c1-3 7-3 8 0" fill="#fff"/></svg>
  <svg class="a" style="left:92px;top:229px" width="16" height="16"><path d="M8 1l6 2v5c0 4-3 6-6 7-3-1-6-3-6-7V3z" fill="#fff"/><path d="M5 8l2 2 4-4" stroke="#1287f0" stroke-width="1.3" fill="none"/></svg>
  <svg class="a" style="left:159px;top:229px" width="16" height="16"><path d="M8 1l6 2v5c0 4-3 6-6 7-3-1-6-3-6-7V3z" fill="none" stroke="#fff"/><circle cx="8" cy="8" r="3" fill="none" stroke="#fff"/></svg>
  <div class="a white center" style="left:2px;top:252px;width:60px;font-size:5px;line-height:1.3;font-weight:600">Min. 5 Years<br>Experience</div>
  <div class="a white center" style="left:70px;top:252px;width:60px;font-size:5px;line-height:1.3;font-weight:600">Vetted &amp;<br>Verified</div>
  <div class="a white center" style="left:137px;top:252px;width:60px;font-size:5px;line-height:1.3;font-weight:600">Fully<br>Insured</div>
  <div class="btn btn-fill" style="left:77px;top:283px;width:49px;height:19px;font-size:5px">Learn More</div>

  <div class="a h center" style="left:10px;top:328px;width:184px;font-size:13px">We’re like Zarvo — but<br>for plumbers.</div>

  <div class="icon-ring" style="left:80px;top:380px;width:44px;height:44px"><svg width="14" height="12"><rect x="1" y="3" width="8" height="7" rx="1" fill="#1287f0"/><circle cx="11" cy="3" r="2" fill="#7bb8f5"/></svg></div>
  <div class="num" style="left:112px;top:380px;width:11px;height:11px">01</div>
  <div class="a h center" style="left:0;top:432px;width:204px;font-size:6.5px">Select Your Issue</div>
  <div class="a p center" style="left:20px;top:444px;width:164px;font-size:4.6px">Choose the plumbing problem you’re facing—leaks, clogs, heating, or anything else.</div>

  <div class="icon-ring" style="left:80px;top:477px;width:44px;height:44px"><svg width="14" height="12"><path d="M2 7l6-6 5 5-6 6z" fill="#1287f0"/></svg></div>
  <div class="num" style="left:112px;top:477px;width:11px;height:11px">02</div>
  <div class="a h center" style="left:0;top:529px;width:204px;font-size:6.5px">View Upfront Pricing</div>
  <div class="a p center" style="left:40px;top:541px;width:124px;font-size:4.6px">Get instant, transparent pricing with no hidden charges.</div>

  <div class="icon-ring" style="left:80px;top:574px;width:44px;height:44px"><svg width="8" height="14"><rect x="0" y="0" width="8" height="14" rx="1.5" fill="#1287f0"/></svg></div>
  <div class="num" style="left:112px;top:574px;width:11px;height:11px">03</div>
  <div class="a h center" style="left:0;top:626px;width:204px;font-size:6.5px">Book Instantly</div>
  <div class="a p center" style="left:40px;top:638px;width:124px;font-size:4.6px">Confirm your booking and get matched with a nearby trusted plumber.</div>

  <div class="icon-ring" style="left:80px;top:671px;width:44px;height:44px"><svg width="10" height="14"><rect x="0" y="0" width="9" height="14" rx="1.5" fill="#1287f0"/><circle cx="4.5" cy="6" r="2" fill="#fff"/></svg></div>
  <div class="num" style="left:112px;top:671px;width:11px;height:11px">04</div>
  <div class="a h center" style="left:0;top:723px;width:204px;font-size:6.5px">Track in Real-Time</div>
  <div class="a p center" style="left:56px;top:735px;width:92px;font-size:4.6px">Watch your plumber’s live location as they head to your doorstep.</div>

  <div class="a h center" style="left:0;top:794px;width:208px;font-size:13px">Our Core Services</div>

  <div class="card" style="left:33px;top:827px;width:139px;height:168px"></div>
  <div class="photo" role="img" aria-label="Plumber tightening a chrome pipe with a wrench" style="left:39px;top:833px;width:127px;height:73px"></div>
  <div class="stripe" style="left:39px;top:906px;width:95px"></div>
  <div class="a" style="left:39px;top:890px;width:16px;height:16px;background:var(--blue)"></div>
  <div class="a h" style="left:39px;top:924px;font-size:7px">Plumbing</div>
  <div class="a p" style="left:39px;top:943px;width:128px;font-size:4.6px">Fixing everything from dripping taps to major pipe bursts and blocked toilets—fast and reliable.</div>
  <div class="a blue" style="left:39px;top:980px;font-size:4px;font-weight:700">LEARN MORE</div>

  <div class="card" style="left:33px;top:1003px;width:139px;height:168px"></div>
  <div class="photo" role="img" aria-label="Plumber clearing a blocked drain under a sink" style="left:39px;top:1009px;width:127px;height:73px"></div>
  <div class="stripe" style="left:39px;top:1082px;width:95px"></div>
  <div class="a" style="left:39px;top:1066px;width:16px;height:16px;background:var(--blue)"></div>
  <div class="a h" style="left:39px;top:1100px;font-size:7px">Drainage</div>
  <div class="a p" style="left:39px;top:1119px;width:128px;font-size:4.6px">We clear blocked drains, overflowing systems, and bad smells with expert care and modern tools.</div>
  <div class="a blue" style="left:39px;top:1156px;font-size:4px;font-weight:700">LEARN MORE</div>

  <div class="card" style="left:33px;top:1179px;width:139px;height:166px"></div>
  <div class="photo" role="img" aria-label="Engineer servicing a wall-mounted boiler" style="left:39px;top:1185px;width:127px;height:73px"></div>
  <div class="stripe" style="left:39px;top:1258px;width:95px"></div>
  <div class="a" style="left:39px;top:1242px;width:16px;height:16px;background:var(--blue)"></div>
  <div class="a h" style="left:39px;top:1276px;font-size:7px">Heating</div>
  <div class="a p" style="left:39px;top:1295px;width:128px;font-size:4.6px">Expert repairs and installations for radiators, boilers, and central heating systems to keep your home warm.</div>
  <div class="a blue" style="left:39px;top:1331px;font-size:4px;font-weight:700">LEARN MORE</div>

  <div class="map" role="img" aria-label="Street map with nearby plumber vans" style="left:32px;top:1368px;width:148px;height:100px;border-radius:3px"></div>
  <div class="a" style="left:32px;top:1478px;width:148px;height:82px;background:var(--blue);border-radius:3px"></div>
  <div class="a h white" style="left:41px;top:1492px;font-size:10px;line-height:1.15">Call an PipeDashly<br>Now</div>
  <div class="a white" style="left:41px;top:1519px;font-size:3.2px;opacity:.85">We have local plumbers near you—ready to assist 24/7, day or night.</div>
  <div class="btn" style="left:41px;top:1532px;width:54px;height:13px;background:#fff;color:var(--blue);border-radius:7px;font-size:3.5px">CALL A PLUMBER NOW</div>

  <div class="map map-river" role="img" aria-label="Map of London with the Thames" style="left:23px;top:1585px;width:149px;height:121px"></div>
  <div class="a h center" style="left:0;top:1716px;width:204px;font-size:13px">Expanding Across<br>London &amp; Essex</div>
  <div class="a p center" style="left:22px;top:1755px;width:160px;font-size:4.6px">We’re growing fast—now serving all major boroughs across London and Essex with trusted, on-call plumbers ready to help 24/7.</div>
  <div class="a h" style="left:38px;top:1797px;font-size:6.3px">Central &amp; North London</div>
  <div class="chev" style="left:169px;top:1798px;width:8px;height:8px"></div>
  <div class="check" style="left:38px;top:1814px"></div><div class="a p" style="left:48px;top:1813px;font-size:4.6px">Camden</div>
  <div class="check" style="left:87px;top:1814px"></div><div class="a p" style="left:97px;top:1813px;font-size:4.6px">Islington</div>
  <div class="check" style="left:38px;top:1826px"></div><div class="a p" style="left:48px;top:1825px;font-size:4.6px">Westminster</div>
  <div class="check" style="left:87px;top:1826px"></div><div class="a p" style="left:97px;top:1825px;font-size:4.6px">Haringey</div>
  <div class="check" style="left:38px;top:1838px"></div><div class="a p" style="left:48px;top:1837px;font-size:4.6px">Barnet</div>
  <div class="check" style="left:87px;top:1838px"></div><div class="a p" style="left:97px;top:1837px;font-size:4.6px">Enfield</div>
  <div class="check" style="left:38px;top:1850px"></div><div class="a p" style="left:48px;top:1849px;font-size:4.6px">Hackney</div>
  <div class="check" style="left:87px;top:1850px"></div><div class="a p" style="left:97px;top:1849px;font-size:4.6px">Hammersmith</div>
  <div class="a h" style="left:38px;top:1865px;font-size:6.3px">East London</div>
  <div class="a h" style="left:38px;top:1882px;font-size:6.3px">South London</div>
  <div class="a h" style="left:38px;top:1899px;font-size:6.3px">West London</div>
</section>

<!-- ============ MOBILE: lower section ============ -->
<section class="artboard mobile-bottom" style="left:402px;top:545px;width:204px;height:1679px">
  <div class="a h center" style="left:0;top:4px;width:204px;font-size:13px">Why Customers Love<br>PipeDashly</div>
  <div class="a p center" style="left:28px;top:45px;width:148px;font-size:4.6px">We’re built around speed, transparency, and trust—here’s why thousands of Londoners choose us:</div>
  <div class="icon-ring" style="left:12px;top:68px;width:14px;height:14px;background:var(--tint)"><svg width="7" height="7"><circle cx="3.5" cy="3.5" r="3.2" fill="#1287f0"/></svg></div>
  <div class="a h" style="left:40px;top:66px;font-size:6.3px">Available 24/7</div>
  <div class="a p" style="left:40px;top:78px;font-size:4.4px">Plumbing emergencies don’t wait, and neither do we.</div>
  <div class="icon-ring" style="left:12px;top:96px;width:14px;height:14px;background:var(--tint)"><svg width="7" height="7"><circle cx="3.5" cy="3.5" r="3.2" fill="#1287f0"/></svg></div>
  <div class="a h" style="left:40px;top:94px;font-size:6.3px">Up-Front, Transparent Pricing</div>
  <div class="a p" style="left:40px;top:106px;font-size:4.4px">No guesswork. No hidden fees</div>
  <div class="icon-ring" style="left:12px;top:123px;width:14px;height:14px;background:var(--tint)"><svg width="7" height="7"><circle cx="3.5" cy="3.5" r="3.2" fill="#1287f0"/></svg></div>
  <div class="a h" style="left:40px;top:121px;font-size:6.3px">Immediate Response</div>
  <div class="a p" style="left:40px;top:133px;width:150px;font-size:4.4px">We respond instantly. Book in seconds, get matched with a nearby plumber.</div>
  <div class="btn btn-navy" style="left:55px;top:155px;width:94px;height:19px;font-size:4.6px">Book Your Plumber Now</div>

  <div class="a h" style="left:12px;top:208px;font-size:13px">What Our Customers Say</div>
  <div class="a" style="left:12px;top:235px;width:140px;height:80px;background:var(--tint);border-radius:3px"></div>
  <div class="quote" style="left:27px;top:243px;font-size:13px">”</div>
  <div class="a p" style="left:27px;top:266px;width:110px;font-size:4.6px">Was here in under 15 minutes to fix my leak at midnight!</div>
  <div class="a h" style="left:27px;top:291px;font-size:4.6px">Priya, Shoreditch</div>
  <div class="a p" style="left:27px;top:298px;font-size:3px">CLIENT, UK</div>
  <div class="avatar" role="img" aria-label="Customer portrait" style="left:132px;top:294px;width:13px;height:13px"></div>
  <div class="a" style="left:163px;top:235px;width:60px;height:80px;background:var(--tint);border-radius:3px"></div>
  <div class="quote" style="left:177px;top:243px;font-size:13px">”</div>
  <div class="a p" style="left:177px;top:266px;font-size:4.6px">“I booked</div>
  <div class="a h" style="left:177px;top:291px;font-size:4.6px">Daniel Hart</div>
  <div class="a" style="left:6px;top:265px;width:13px;height:13px;border-radius:50%;background:var(--navy)"></div>
  <div class="a" style="left:187px;top:265px;width:13px;height:13px;border-radius:50%;background:var(--navy)"></div>
  <div class="badge-shape" style="left:56px;top:331px;width:14px;height:12px;background:#e8d94a"></div>
  <div class="badge-shape" style="left:111px;top:334px;width:26px;height:6px"></div>
  <div class="badge-shape" style="left:186px;top:334px;width:18px;height:6px;background:#d8475a"></div>

  <div class="a h center" style="left:0;top:387px;width:204px;font-size:13px">Frequently Asked<br>Questions</div>
  <div class="a p center" style="left:30px;top:427px;width:144px;font-size:4.6px">We’ve answered the most common questions to help you book with confidence.</div>
  <div class="a h" style="left:11px;top:455px;width:150px;font-size:6px">How can I verify that PipeDashly plumbers are reliable?</div>
  <div class="chev" style="left:177px;top:474px;width:9px;height:9px"></div>
  <div class="a p" style="left:11px;top:482px;width:160px;font-size:4.3px">All our plumbers are vetted, reviewed, and rated by real customers. We only work with trusted, experienced professionals.</div>
  <div class="a h" style="left:11px;top:515px;width:150px;font-size:6px">Are your plumbers registered with HeatMark?</div>
  <div class="chev" style="left:178px;top:521px;width:9px;height:9px"></div>
  <div class="a h" style="left:11px;top:544px;font-size:6px">Do your plumbers have insurance?</div>
  <div class="chev" style="left:178px;top:544px;width:9px;height:9px"></div>
  <div class="a h" style="left:13px;top:562px;font-size:6px">How much do your plumbers cost?</div>
  <div class="chev" style="left:178px;top:562px;width:9px;height:9px"></div>
  <div class="a h" style="left:11px;top:580px;font-size:6px">Do you charge a call-out fee?</div>
  <div class="chev" style="left:178px;top:580px;width:9px;height:9px"></div>

  <div class="a h center" style="left:8px;top:624px;width:204px;font-size:13px">From the PipeDashly<br>Blog</div>
  <div class="card" style="left:28px;top:680px;width:147px;height:158px"></div>
  <div class="photo" role="img" aria-label="Gloved hands using a wrench on pipework" style="left:28px;top:680px;width:147px;height:103px"></div>
  <div class="a blue" style="left:118px;top:773px;font-size:3.2px;background:#fff;padding:1px 4px">16 OCT 2024</div>
  <div class="a h" style="left:40px;top:797px;width:130px;font-size:6px">Top 5 Signs You Need a Plumber – Before It’s Too Late</div>
  <div class="a p" style="left:40px;top:820px;font-size:4px">PLUMBER &nbsp;/&nbsp; LENA VOSS</div>
  <div class="card" style="left:28px;top:849px;width:147px;height:156px"></div>
  <div class="photo photo-warm" role="img" aria-label="Plumber kneeling by a kitchen cabinet with a toolbox" style="left:28px;top:849px;width:147px;height:102px"></div>
  <div class="a blue" style="left:118px;top:941px;font-size:3.2px;background:#fff;padding:1px 4px">16 OCT 2024</div>
  <div class="a h" style="left:40px;top:966px;width:130px;font-size:6px">Boiler Not Working? Try These Quick Fixes First</div>
  <div class="a p" style="left:40px;top:989px;font-size:4px">SPECIAL REPAIRS &nbsp;/&nbsp; LENA VOSS</div>
  <div class="card" style="left:28px;top:1018px;width:147px;height:157px"></div>
  <div class="photo" role="img" aria-label="Hands working under a kitchen tap" style="left:28px;top:1018px;width:147px;height:102px"></div>
  <div class="a blue" style="left:118px;top:1110px;font-size:3.2px;background:#fff;padding:1px 4px">16 OCT 2024</div>
  <div class="a h" style="left:40px;top:1135px;width:130px;font-size:6px">How to Unblock a Drain – Safely and Effectively</div>
  <div class="a p" style="left:40px;top:1158px;font-size:4px">HANDYMAN &nbsp;/&nbsp; TOM HALE</div>

  <div class="footer" style="left:0;top:1208px;width:204px;height:471px">
    <div class="a center" style="left:0;top:22px;width:204px;display:flex;justify-content:center;align-items:center;gap:3px;color:#fff;font-weight:700;font-size:17px"><span style="display:block;width:8px;height:16px;background:var(--blue)"></span>PipeDashly</div>
    <div class="a center" style="left:0;top:56px;width:204px;font-size:5.5px;line-height:1.5">Created with ♥ in London<br>Registered in England &amp; Wales<br>Company No. 999888877<br>ICO Registration No. AB9876543<br>ISO27001 Compliant</div>
    <div class="social" style="left:68px;top:118px"></div><div class="social" style="left:86px;top:118px"></div><div class="social" style="left:106px;top:118px"></div><div class="social" style="left:126px;top:118px"></div>
    <div class="a center white" style="left:0;top:146px;width:204px;font-size:15px;font-weight:600;line-height:1.7">Need a Plumber<br>Right Now?</div>
    <div class="btn" style="left:14px;top:210px;width:100px;height:24px;border:1px solid #fff;border-radius:12px;color:#fff;font-size:5px">◉&nbsp; Find a Plumber Near Me</div>
    <div class="btn" style="left:120px;top:210px;width:70px;height:24px;background:#fff;border-radius:12px;color:var(--navy);font-size:5px">☎&nbsp; 0800-555-0199</div>
    <div class="a white" style="left:16px;top:266px;font-size:7px;font-weight:600">Useful Link</div>
    <div class="a" style="left:16px;top:282px;font-size:5px;line-height:2.95">Home<br>How It Works<br>Services<br>Pricing<br>FAQs<br>Contact</div>
    <div class="a white" style="left:94px;top:266px;font-size:7px;font-weight:600">Legal Links</div>
    <div class="a" style="left:94px;top:282px;font-size:5px;line-height:2.95">Privacy &amp; Cookie Policy<br>Terms &amp; Conditions<br>Service Terms &amp; Conditions<br>Complaints Policy<br>Other Policy</div>
    <div class="a white" style="left:16px;top:382px;font-size:9px;font-weight:600">Contact</div>
    <div class="a" style="left:16px;top:400px;font-size:5.5px;line-height:1.5">48 Harbour Lane<br>London, E2 7QP, UK</div>
    <div class="a center" style="left:0;top:437px;width:204px;font-size:5.5px">© PipeDashly Services Ltd. All Rights Reserved.</div>
  </div>
</section>

<!-- ============ DESKTOP ============ -->
<section class="artboard desktop" style="left:738px;top:0;width:642px;height:2480px">
  <div class="a" style="left:0;top:45px;width:642px;height:1px;background:var(--line)"></div>
  <div class="logo" style="left:92px;top:17px;font-size:8.5px"><i style="width:5px;height:10px"></i>PipeDashly</div>
  <div class="a blue" style="left:222px;top:19px;font-size:6px;font-weight:600">Home</div>
  <div class="a p" style="left:263px;top:19px;font-size:6px">How It Works</div>
  <div class="a p" style="left:325px;top:19px;font-size:6px">Services</div>
  <div class="a p" style="left:371px;top:19px;font-size:6px">FAQs</div>
  <div class="a p" style="left:406px;top:19px;font-size:6px">Contact</div>
  <div class="btn btn-out" style="left:494px;top:14px;width:55px;height:19px;font-size:5.5px">Contact Us</div>

  <div class="photo" role="img" aria-label="Plumber in a blue hard hat repairing pipework" style="left:345px;top:46px;width:297px;height:244px;background:linear-gradient(90deg,#fff 0%,#e3e6ea 18%,#a4adb8 55%,#3a4a63)"></div>
  <div class="a h" style="left:93px;top:112px;font-size:20px">Plumbing Emergency?</div>
  <div class="a h blue" style="left:93px;top:140px;font-size:20px">Get Help in Minutes.</div>
  <div class="a p" style="left:93px;top:173px;width:200px;font-size:5.5px">Book a trusted, local plumber near you—available 24/7 with instant response and up-front pricing. No delays. No surprises.</div>
  <div class="btn btn-out" style="left:93px;top:206px;width:73px;height:20px;font-size:5.5px">Get Instant Help</div>
  <div class="btn btn-fill" style="left:172px;top:206px;width:88px;height:20px;font-size:5.5px">Book a Plumber Now</div>

  <div class="a" style="left:0;top:290px;width:257px;height:117px;background:var(--navy)"></div>
  <div class="a" style="left:257px;top:290px;width:385px;height:117px;background:var(--blue)"></div>
  <div class="a h white" style="left:93px;top:313px;font-size:15px">Why Choose<br>PipeDashly?</div>
  <div class="btn btn-fill" style="left:93px;top:366px;width:57px;height:19px;font-size:5.5px">Learn More</div>
  <svg class="a" style="left:302px;top:318px" width="28" height="28"><circle cx="14" cy="14" r="12" fill="none" stroke="#fff" stroke-width="1.3"/><circle cx="14" cy="11" r="4" fill="#fff"/><path d="M7 21c2-5 12-5 14 0" fill="#fff"/></svg>
  <svg class="a" style="left:402px;top:318px" width="28" height="28"><path d="M14 2l10 4v8c0 6-5 10-10 12-5-2-10-6-10-12V6z" fill="#fff"/><path d="M9 14l3.5 3.5 7-7" stroke="#1287f0" stroke-width="2" fill="none"/></svg>
  <svg class="a" style="left:502px;top:318px" width="28" height="28"><path d="M14 2l10 4v8c0 6-5 10-10 12-5-2-10-6-10-12V6z" fill="none" stroke="#fff" stroke-width="1.3"/><circle cx="14" cy="13" r="5" fill="none" stroke="#fff" stroke-width="1.3"/></svg>
  <div class="a white center" style="left:276px;top:353px;width:80px;font-size:8.5px;line-height:1.3">Min. 5 Years<br>Experience</div>
  <div class="a white center" style="left:376px;top:353px;width:80px;font-size:8.5px;line-height:1.3">Vetted &amp;<br>Verified</div>
  <div class="a white center" style="left:476px;top:353px;width:80px;font-size:8.5px;line-height:1.3">Fully<br>Insured</div>

  <div class="pill" style="left:298px;top:440px">HOW IT WORKS</div>
  <div class="a h center" style="left:0;top:451px;width:642px;font-size:15.5px">We’re like Zarvo — but for plumbers.<br>Simple, fast, and reliable.</div>
  <div class="rule" style="left:142px;top:522px;width:362px"></div>
  <div class="icon-ring" style="left:128px;top:508px;width:28px;height:28px"><svg width="10" height="9"><rect x="0" y="2" width="7" height="6" fill="#1287f0"/></svg></div>
  <div class="num" style="left:150px;top:505px;width:9px;height:9px;font-size:3px">01</div>
  <div class="icon-ring" style="left:250px;top:508px;width:28px;height:28px"><svg width="10" height="9"><path d="M1 6l5-5 4 4-5 4z" fill="#1287f0"/></svg></div>
  <div class="num" style="left:272px;top:505px;width:9px;height:9px;font-size:3px">02</div>
  <div class="icon-ring" style="left:370px;top:508px;width:28px;height:28px"><svg width="6" height="10"><rect width="6" height="10" rx="1" fill="#1287f0"/></svg></div>
  <div class="num" style="left:392px;top:505px;width:9px;height:9px;font-size:3px">03</div>
  <div class="icon-ring" style="left:490px;top:508px;width:28px;height:28px"><svg width="7" height="10"><rect width="7" height="10" rx="1" fill="#1287f0"/><circle cx="3.5" cy="4" r="1.5" fill="#fff"/></svg></div>
  <div class="num" style="left:512px;top:505px;width:9px;height:9px;font-size:3px">04</div>
  <div class="a h center" style="left:92px;top:548px;width:100px;font-size:7px">Select Your Issue</div>
  <div class="a p center" style="left:92px;top:562px;width:100px;font-size:5px">Choose the plumbing problem you’re facing—leaks, clogs, heating, or anything else.</div>
  <div class="a h center" style="left:214px;top:548px;width:100px;font-size:7px">View Upfront Pricing</div>
  <div class="a p center" style="left:214px;top:562px;width:100px;font-size:5px">Get instant, transparent pricing with no hidden charges.</div>
  <div class="a h center" style="left:334px;top:548px;width:100px;font-size:7px">Book Instantly</div>
  <div class="a p center" style="left:334px;top:562px;width:100px;font-size:5px">Confirm your booking and get matched with a nearby trusted plumber.</div>
  <div class="a h center" style="left:454px;top:548px;width:100px;font-size:7px">Track in Real-Time</div>
  <div class="a p center" style="left:454px;top:562px;width:100px;font-size:5px">Watch your plumber’s live location as they head to your doorstep.</div>

  <div class="a" style="left:0;top:621px;width:642px;height:224px;background:var(--tint)"></div>
  <div class="a h center" style="left:0;top:637px;width:646px;font-size:15.5px">Our Core Services</div>
  <div class="card" style="left:116px;top:666px;width:124px;height:152px"></div>
  <div class="photo" role="img" aria-label="Wrench on a chrome pipe joint" style="left:123px;top:673px;width:116px;height:67px"></div>
  <div class="a" style="left:123px;top:726px;width:14px;height:14px;background:var(--blue)"></div>
  <div class="stripe" style="left:123px;top:740px;width:88px;height:5px"></div>
  <div class="a h" style="left:123px;top:754px;font-size:9px">Plumbing</div>
  <div class="a p" style="left:123px;top:772px;width:112px;font-size:4.8px">Fixing everything from dripping taps to major pipe bursts and blocked toilets—fast and reliable.</div>
  <div class="a blue" style="left:123px;top:806px;font-size:3.8px;font-weight:700">LEARN MORE</div>
  <div class="card" style="left:255px;top:666px;width:124px;height:152px"></div>
  <div class="photo" role="img" aria-label="Plumber clearing a blocked drain" style="left:262px;top:673px;width:116px;height:67px"></div>
  <div class="a" style="left:262px;top:726px;width:14px;height:14px;background:var(--blue)"></div>
  <div class="stripe" style="left:262px;top:740px;width:88px;height:5px"></div>
  <div class="a h" style="left:262px;top:754px;font-size:9px">Drainage</div>
  <div class="a p" style="left:262px;top:772px;width:112px;font-size:4.8px">We clear blocked drains, overflowing systems, and bad smells with expert care and modern tools.</div>
  <div class="a blue" style="left:262px;top:806px;font-size:3.8px;font-weight:700">LEARN MORE</div>
  <div class="card" style="left:394px;top:666px;width:124px;height:152px"></div>
  <div class="photo" role="img" aria-label="Engineer repairing a boiler" style="left:401px;top:673px;width:116px;height:67px"></div>
  <div class="a" style="left:401px;top:726px;width:14px;height:14px;background:var(--blue)"></div>
  <div class="stripe" style="left:401px;top:740px;width:88px;height:5px"></div>
  <div class="a h" style="left:401px;top:754px;font-size:9px">Heating</div>
  <div class="a p" style="left:401px;top:772px;width:112px;font-size:4.8px">Expert repairs and installations for radiators, boilers, and central heating systems to keep your home warm.</div>
  <div class="a blue" style="left:401px;top:806px;font-size:3.8px;font-weight:700">LEARN MORE</div>

  <div class="map" role="img" aria-label="Street map with nearby plumber vans" style="left:116px;top:878px;width:176px;height:115px;border-radius:4px"></div>
  <div class="a" style="left:303px;top:878px;width:222px;height:115px;background:var(--blue);border-radius:4px"></div>
  <div class="a h white" style="left:316px;top:895px;font-size:15px;line-height:1.15">Call an PipeDashly<br>Now</div>
  <div class="a white" style="left:316px;top:938px;font-size:5px;opacity:.85">We have local plumbers near you—ready to assist 24/7, day or night.</div>
  <div class="btn" style="left:316px;top:956px;width:82px;height:18px;background:#fff;color:var(--blue);border-radius:9px;font-size:4.8px">CALL A PLUMBER NOW</div>

  <div class="a" style="left:0;top:1028px;width:642px;height:199px;background:var(--tint)"></div>
  <div class="map map-river" role="img" aria-label="Map of London boroughs with the Thames" style="left:104px;top:1043px;width:206px;height:169px"></div>
  <div class="a h" style="left:332px;top:1040px;font-size:15px">Expanding Across London<br>&amp; Essex</div>
  <div class="a p" style="left:332px;top:1082px;width:190px;font-size:5px">We’re growing fast—now serving all major boroughs across London and Essex with trusted, on-call plumbers ready to help 24/7.</div>
  <div class="a h" style="left:332px;top:1118px;font-size:6.5px">Central &amp; North London</div>
  <div class="a" style="left:506px;top:1118px;font-size:5px">⌄</div>
  <div class="check" style="left:332px;top:1135px"></div><div class="a p" style="left:342px;top:1135px;font-size:4.8px">Camden</div>
  <div class="check" style="left:380px;top:1135px"></div><div class="a p" style="left:390px;top:1135px;font-size:4.8px">Islington</div>
  <div class="check" style="left:428px;top:1135px"></div><div class="a p" style="left:438px;top:1135px;font-size:4.8px">Westminster</div>
  <div class="check" style="left:476px;top:1135px"></div><div class="a p" style="left:486px;top:1135px;font-size:4.8px">Haringey</div>
  <div class="check" style="left:332px;top:1149px"></div><div class="a p" style="left:342px;top:1149px;font-size:4.8px">Barnet</div>
  <div class="check" style="left:380px;top:1149px"></div><div class="a p" style="left:390px;top:1149px;font-size:4.8px">Enfield</div>
  <div class="check" style="left:428px;top:1149px"></div><div class="a p" style="left:438px;top:1149px;font-size:4.8px">Hackney</div>
  <div class="check" style="left:476px;top:1149px"></div><div class="a p" style="left:486px;top:1149px;font-size:4.8px">Hammersmith</div>
  <div class="a h" style="left:332px;top:1167px;font-size:6.5px">East London</div>
  <div class="a h" style="left:332px;top:1186px;font-size:6.5px">South London</div>
  <div class="a h" style="left:332px;top:1206px;font-size:6.5px">West London</div>

  <div class="photo photo-warm" role="img" aria-label="Smiling plumber in blue overalls fixing a sink" style="left:102px;top:1268px;width:192px;height:175px;border-radius:3px"></div>
  <div class="a" style="left:102px;top:1395px;width:60px;height:48px;background:var(--blue);border-radius:3px"></div>
  <div class="a white" style="left:110px;top:1401px;font-size:13px;font-weight:600">25+</div>
  <div class="a white" style="left:110px;top:1421px;font-size:4px;opacity:.9">Years as a Trusted<br>Provider</div>
  <div class="pill" style="left:322px;top:1262px">OUR EXPERIENCE</div>
  <div class="a h" style="left:322px;top:1272px;font-size:15px;line-height:1.15">Why Customers Love<br>PipeDashly</div>
  <div class="a p" style="left:322px;top:1312px;width:180px;font-size:5px">We’re built around speed, transparency, and trust—here’s why thousands of Londoners choose us:</div>
  <div class="icon-ring" style="left:322px;top:1338px;width:18px;height:18px;background:var(--tint)"><svg width="9" height="9"><circle cx="4.5" cy="4.5" r="4" fill="#1287f0"/></svg></div>
  <div class="a h" style="left:355px;top:1336px;font-size:6.5px">Available 24/7</div>
  <div class="a p" style="left:355px;top:1350px;font-size:4.8px">Plumbing emergencies don’t wait, and neither do we.</div>
  <div class="icon-ring" style="left:322px;top:1369px;width:18px;height:18px;background:var(--tint)"><svg width="9" height="9"><circle cx="4.5" cy="4.5" r="4" fill="#1287f0"/></svg></div>
  <div class="a h" style="left:355px;top:1367px;font-size:6.5px">Up-Front, Transparent Pricing</div>
  <div class="a p" style="left:355px;top:1381px;font-size:4.8px">No guesswork. No hidden fees</div>
  <div class="icon-ring" style="left:322px;top:1400px;width:18px;height:18px;background:var(--tint)"><svg width="9" height="9"><circle cx="4.5" cy="4.5" r="4" fill="#1287f0"/></svg></div>
  <div class="a h" style="left:355px;top:1398px;font-size:6.5px">Immediate Response</div>
  <div class="a p" style="left:355px;top:1412px;width:170px;font-size:4.8px">We respond instantly. Book in seconds, get matched with a nearby plumber.</div>
  <div class="btn btn-navy" style="left:322px;top:1433px;width:87px;height:17px;font-size:4.8px">Book Your Plumber Now</div>

  <div class="pill" style="left:93px;top:1484px">TESTIMONIALS</div>
  <div class="a h" style="left:93px;top:1494px;font-size:15px">What Our Customers Say</div>
  <div class="a" style="left:520px;top:1497px;width:29px;height:16px;border-radius:8px;background:var(--navy)"></div>
  <div class="a white" style="left:525px;top:1499px;font-size:7px;letter-spacing:5px">‹›</div>
  <div class="a" style="left:93px;top:1532px;width:212px;height:122px;background:var(--tint);border-radius:4px"></div>
  <div class="quote" style="left:114px;top:1544px;font-size:22px">”</div>
  <div class="a p" style="left:117px;top:1581px;width:180px;font-size:7px">Was here in under 15 minutes to fix my leak at midnight!</div>
  <div class="a h" style="left:117px;top:1621px;font-size:6px">Priya, Shoreditch</div>
  <div class="a p" style="left:117px;top:1631px;font-size:3.5px">CLIENT, UK</div>
  <div class="avatar" role="img" aria-label="Customer portrait" style="left:272px;top:1621px;width:22px;height:22px"></div>
  <div class="a" style="left:337px;top:1532px;width:212px;height:122px;background:var(--tint);border-radius:4px"></div>
  <div class="quote" style="left:358px;top:1544px;font-size:22px">”</div>
  <div class="a p" style="left:361px;top:1581px;width:180px;font-size:7px">“I booked online and my boiler was repaired in an hour. Impressive response time!</div>
  <div class="a h" style="left:361px;top:1621px;font-size:6px">Daniel Hart</div>
  <div class="a p" style="left:361px;top:1631px;font-size:3.5px">CLIENT, UK</div>
  <div class="avatar" role="img" aria-label="Customer portrait" style="left:516px;top:1626px;width:22px;height:22px"></div>
  <div class="rule" style="left:93px;top:1684px;width:456px"></div>
  <div class="badge-shape" style="left:106px;top:1709px;width:32px;height:16px"></div>
  <div class="badge-shape" style="left:204px;top:1706px;width:18px;height:22px;background:#e8d94a"></div>
  <div class="badge-shape" style="left:300px;top:1714px;width:40px;height:7px"></div>
  <div class="badge-shape" style="left:396px;top:1710px;width:46px;height:16px;background:#d8475a"></div>
  <div class="badge-shape" style="left:494px;top:1706px;width:18px;height:22px;background:#e8d94a"></div>

  <div class="pill" style="left:312px;top:1774px">FAQ</div>
  <div class="a h center" style="left:0;top:1783px;width:652px;font-size:15px">Frequently Asked Questions</div>
  <div class="a p center" style="left:226px;top:1803px;width:196px;font-size:5px">We’ve answered the most common questions to help you book with confidence.</div>
  <div class="a h" style="left:122px;top:1830px;font-size:6.5px;font-weight:400;color:var(--ink)">How can I verify that PipeDashly plumbers are reliable?</div>
  <div class="chev" style="left:516px;top:1835px"></div>
  <div class="a p" style="left:122px;top:1848px;width:300px;font-size:4.8px">All our plumbers are vetted, reviewed, and rated by real customers. We only work with trusted, experienced professionals.</div>
  <div class="a h" style="left:122px;top:1887px;font-size:6.5px;font-weight:400;color:var(--ink)">Are your plumbers registered with HeatMark?</div>
  <div class="chev" style="left:516px;top:1886px"></div>
  <div class="a h" style="left:122px;top:1918px;font-size:6.5px;font-weight:400;color:var(--ink)">Do your plumbers have insurance?</div>
  <div class="chev" style="left:516px;top:1918px"></div>
  <div class="a h" style="left:124px;top:1950px;font-size:6.5px;font-weight:400;color:var(--ink)">How much do your plumbers cost?</div>
  <div class="chev" style="left:516px;top:1950px"></div>
  <div class="a h" style="left:122px;top:1982px;font-size:6.5px;font-weight:400;color:var(--ink)">Do you charge a call-out fee?</div>
  <div class="chev" style="left:516px;top:1981px"></div>

  <div class="pill" style="left:99px;top:2030px">RECENT BLOG</div>
  <div class="a h" style="left:99px;top:2039px;font-size:15px">From the PipeDashly Blog</div>
  <div class="btn" style="left:496px;top:2040px;width:60px;height:18px;border:1px solid var(--ink);border-radius:9px;font-size:4px">VIEW ALL POST</div>
  <div class="card" style="left:93px;top:2073px;width:145px;height:155px"></div>
  <div class="photo" role="img" aria-label="Gloved hands using a wrench on pipework" style="left:93px;top:2073px;width:145px;height:100px"></div>
  <div class="a blue" style="left:180px;top:2164px;font-size:3.2px;background:#fff;padding:1px 4px">16 OCT 2024</div>
  <div class="a h" style="left:105px;top:2188px;width:130px;font-size:6.5px">Top 5 Signs You Need a Plumber – Before It’s Too Late</div>
  <div class="a p" style="left:105px;top:2212px;font-size:3.8px">PLUMBER / LENA VOSS</div>
  <div class="card" style="left:248px;top:2073px;width:146px;height:155px"></div>
  <div class="photo photo-warm" role="img" aria-label="Plumber kneeling by a kitchen cabinet" style="left:248px;top:2073px;width:146px;height:100px"></div>
  <div class="a blue" style="left:336px;top:2164px;font-size:3.2px;background:#fff;padding:1px 4px">16 OCT 2024</div>
  <div class="a h" style="left:260px;top:2188px;width:130px;font-size:6.5px">Boiler Not Working? Try These Quick Fixes First</div>
  <div class="a p" style="left:260px;top:2212px;font-size:3.8px">SPECIAL REPAIRS / LENA VOSS</div>
  <div class="card" style="left:403px;top:2073px;width:146px;height:155px"></div>
  <div class="photo" role="img" aria-label="Hands working under a kitchen tap" style="left:403px;top:2073px;width:146px;height:100px"></div>
  <div class="a blue" style="left:491px;top:2164px;font-size:3.2px;background:#fff;padding:1px 4px">16 OCT 2024</div>
  <div class="a h" style="left:415px;top:2188px;width:130px;font-size:6.5px">How to Unblock a Drain – Safely and Effectively</div>
  <div class="a p" style="left:415px;top:2212px;font-size:3.8px">HANDYMAN / TOM HALE</div>

  <div class="footer" style="left:0;top:2256px;width:642px;height:224px">
    <div class="a" style="left:100px;top:38px;display:flex;align-items:center;gap:2px;color:#fff;font-weight:700;font-size:11px"><span style="display:block;width:5px;height:11px;background:var(--blue)"></span>PipeDashly</div>
    <div class="a" style="left:100px;top:66px;font-size:4px;line-height:1.5">Created with ♥ in London<br>Registered in England &amp; Wales<br>Company No. 999888877<br>ICO Registration No. AB9876543<br>ISO27001 Compliant</div>
    <div class="social" style="left:100px;top:107px;width:4px;height:4px"></div><div class="social" style="left:112px;top:107px;width:4px;height:4px"></div><div class="social" style="left:126px;top:107px;width:4px;height:4px"></div><div class="social" style="left:140px;top:107px;width:4px;height:4px"></div>
    <div class="a white" style="left:255px;top:36px;font-size:9px;font-weight:600">Need a Plumber Right Now?</div>
    <div class="a" style="left:255px;top:53px;width:140px;font-size:4px">We’ve got professionals on-call 24/7 across London. Get fast, affordable plumbing help today.</div>
    <div class="btn" style="left:410px;top:41px;width:74px;height:18px;border:1px solid #fff;border-radius:9px;color:#fff;font-size:3.8px">◉ Find a Plumber Near Me</div>
    <div class="btn" style="left:490px;top:41px;width:58px;height:18px;background:#fff;border-radius:9px;color:var(--navy);font-size:3.8px">☎ 0800-555-0199</div>
    <div class="a" style="left:255px;top:84px;width:293px;height:1px;background:#2a4163"></div>
    <div class="a white" style="left:255px;top:104px;font-size:6px;font-weight:600">Useful Link</div>
    <div class="a" style="left:255px;top:115px;font-size:4px;line-height:2.5">Home<br>How It Works<br>Services<br>Pricing<br>FAQs<br>Contact</div>
    <div class="a white" style="left:361px;top:104px;font-size:6px;font-weight:600">Legal Links</div>
    <div class="a" style="left:361px;top:115px;font-size:4px;line-height:2.5">Privacy &amp; Cookie Policy<br>Terms &amp; Conditions<br>Service Terms &amp; Conditions<br>Complaints Policy<br>Other Policy</div>
    <div class="a white" style="left:467px;top:104px;font-size:6px;font-weight:600">Contact</div>
    <div class="a" style="left:467px;top:116px;font-size:4px;line-height:1.5">48 Harbour Lane<br>London, E2 7QP, UK</div>
    <div class="a center" style="left:0;top:207px;width:642px;font-size:4px">© PipeDashly Services Ltd. All Rights Reserved.</div>
  </div>
</section>

</div>
</body>
</html>
```